New Packaging Design Project

Wine packaging redesign. Retail partner requested a redesign of a private label wine. The old label is attached. Our partner liked the Lantern and Briar label and wanted something similar. There will be a logo added to the top of the label

Went on vacation/holiday

```html
<!DOCTYPE html>
<html lang="en">
<head>
<meta charset="utf-8">
<title>Napa Valley Red Blend 2018 – Label</title>
<link href="https://fonts.googleapis.com/css2?family=Cinzel:wght@400;500&family=Montserrat:wght@400&display=swap" rel="stylesheet">
<style>
  :root {
    --page-bg: #ffffff;
    --label-paper: #efefed;
    --ink-navy: #1f2a38;
    --ink-slate: #6e7a84;
    --ink-wine: #a3192b;
    --range-dark: #1e2936;
    --range-light: #e4e5e3;
  }
  * { margin: 0; padding: 0; box-sizing: border-box; }
  html, body {
    width: 1200px;
    height: 2682px;
    overflow: hidden;
    background: var(--page-bg);
  }
  .canvas {
    position: relative;
    width: 1200px;
    height: 2682px;
  }
  .label {
    position: absolute;
    left: 100px;
    top: 790px;
    width: 1000px;
    height: 1103px;
    background: var(--label-paper);
    overflow: hidden;
  }
  .label__region {
    position: absolute;
    left: 0;
    width: 100%;
    top: 240px;
    text-align: center;
    font-family: "Cinzel", serif;
    font-weight: 400;
    font-size: 104px;
    letter-spacing: 6px;
    line-height: 1;
    color: var(--ink-navy);
    padding-left: 30px;
  }
  .label__varietals {
    position: absolute;
    left: 0;
    width: 100%;
    top: 384px;
    text-align: center;
    font-family: "Montserrat", sans-serif;
    font-size: 22px;
    letter-spacing: 1px;
    line-height: 33px;
    color: var(--ink-slate);
    text-transform: uppercase;
    padding-left: 30px;
  }
  .label__vintage {
    position: absolute;
    left: 750px;
    top: 446px;
    font-family: "Cinzel", serif;
    font-weight: 500;
    font-size: 56px;
    letter-spacing: 4px;
    line-height: 1;
    color: var(--ink-navy);
  }
  .label__style {
    position: absolute;
    left: 138px;
    top: 722px;
    font-family: "Cinzel", serif;
    font-weight: 500;
    font-size: 54px;
    letter-spacing: 7px;
    line-height: 1;
    color: var(--ink-wine);
  }
  .label__range {
    position: absolute;
    left: 0;
    bottom: 0;
    width: 100%;
    height: 290px;
  }
</style>
</head>
<body>
  <main class="canvas">
    <section class="label">
      <h1 class="label__region">Napa Valley</h1>
      <p class="label__varietals">
        Merlot / Cabernet / Sauvignon/<br>
        Cabernet Franc / Petiti Verdot / Malbec
      </p>
      <p class="label__vintage">2018</p>
      <h2 class="label__style">RED BLEND</h2>
      <svg class="label__range" viewBox="0 0 1000 290" preserveAspectRatio="none" role="img" aria-label="Textured illustration of dark mountain ridges above a pale stippled valley floor">
        <defs>
          <linearGradient id="rangeTone" x1="0" y1="0" x2="0" y2="1">
            <stop offset="0" stop-color="var(--range-dark)"/>
            <stop offset="0.45" stop-color="var(--range-dark)"/>
            <stop offset="0.6" stop-color="var(--range-light)"/>
            <stop offset="1" stop-color="var(--range-light)"/>
          </linearGradient>
        </defs>
        <rect x="0" y="0" width="1000" height="290" fill="url(#rangeTone)"/>
      </svg>
    </section>
  </main>
</body>
</html>
```